Translational academic medical clinical group needs website redesign

We have a very rudimentary website that needs a redesign and to be made mobile friendly. We are just finished a logo project and will have a new logo to start the redesign this week. Our current website is k7m4.org. We need a place to profile each researcher in our group, display our publications and have a place to describe current and past projects. It needs to be mobile friendly, have a QRS code that we can print on presentations and posters. It would be nice to have our publications automatically upload from study harbor but we would at least link each researcher to their study harbor profile.

Target Market(s)

Research community and dissemination of published research

Coding

Number of Pages Required

Requirements
Must have
• A profile page for each researcher, a place to link to current publications and study harbor for each researcher, a place to describe current projects. It needs to be mobile friendly.
Nice to have
• It would be fantastic if the publication links can be automatically generated from study harbor.
Should not have
• Open to any suggestions. Avoid pink/purple colours. We are academic and clinical research so University and hospital.

```html
<!DOCTYPE html>
<html lang="en">
<head>
<meta charset="utf-8">
<title>Ward Bridge Care — Critical Care Research</title>
<link href="https://fonts.googleapis.com/css2?family=Montserrat:wght@400;500;600;700;800&display=swap" rel="stylesheet">
<style>
:root{
  --navy:#0b35a3;
  --blue:#1246b4;
  --sky:#4a80d8;
  --ink:#111111;
  --text:#444444;
  --line:#cfcfcf;
  --pale:#dfe9f6;
  --white:#ffffff;
}
*{margin:0;padding:0;box-sizing:border-box}
html,body{width:1200px;height:2533px;overflow:hidden;background:var(--white)}
body{position:relative;font-family:'Montserrat',sans-serif;color:var(--ink)}
.abs{position:absolute}

.site-header{position:absolute;left:0;top:0;width:1200px;height:87px;background:var(--navy)}
.brand{position:absolute;left:145px;top:24px;display:flex;align-items:center;gap:8px;color:var(--white);font-weight:700;font-size:15px;letter-spacing:1px}
.brand-dot{width:38px;height:38px;border-radius:50%;background:#5f8fe0}
.main-nav{position:absolute;left:445px;top:36px;display:flex;gap:30px;font-size:13px;font-weight:600;color:var(--white)}
.main-nav .active{position:relative}
.main-nav .active::after{content:"";position:absolute;left:-3px;right:-3px;top:22px;height:3px;background:#6ea0ea}
.login-btn{position:absolute;left:950px;top:24px;width:106px;height:40px;border-radius:20px;background:var(--sky);color:var(--white);font-size:13px;font-weight:600;display:flex;align-items:center;justify-content:center}

.hero{position:absolute;left:0;top:100px;width:1200px;height:520px}
.hero-dots{position:absolute;top:583px;left:563px;display:flex;gap:7px}
.hero-dots span{width:9px;height:9px;border-radius:50%;background:#a9a9a9}
.hero-dots .on{background:var(--blue)}

.section-title{position:absolute;left:0;width:1200px;text-align:center;font-weight:800;font-size:41px;line-height:58px}
.section-title .sub{display:block;color:var(--blue);font-weight:600}
.title-bar{position:absolute;left:577px;width:46px;height:4px;background:#3d76d2}
.intro{position:absolute;left:0;top:862px;width:1200px;text-align:center;font-size:17px;line-height:29px;color:#333}

.team-card{position:absolute;top:1019px;width:274px;height:414px;border:1px solid var(--line);text-align:center}
.team-photo{position:absolute;left:56px;top:23px;width:162px;height:162px;border-radius:50%}
.team-name{position:absolute;left:0;top:200px;width:272px;font-size:20px;font-weight:600;line-height:30px}
.team-bio{position:absolute;left:10px;top:248px;width:252px;height:84px;overflow:hidden;font-size:12.3px;line-height:21px;color:var(--text)}
.read-btn{position:absolute;left:76px;top:350px;width:121px;height:41px;border-radius:21px;background:var(--navy);color:var(--white);font-size:12px;font-weight:700;display:flex;align-items:center;justify-content:center}

.pub-card{position:absolute;top:1846px;width:292px;height:258px;border:1px solid var(--line);text-align:center}
.pub-date{position:absolute;left:72px;top:0;width:146px;height:38px;background:var(--navy);color:var(--white);font-weight:700;font-size:17px;display:flex;align-items:center;justify-content:center}
.pub-title{margin:76px auto 0;width:250px;font-size:13.5px;font-weight:700;line-height:20px}
.pub-meta{margin:14px auto 0;width:260px;font-size:12px;line-height:20px;color:var(--text)}
.harbor-btn{position:absolute;left:435px;top:2157px;width:330px;height:46px;border-radius:23px;background:var(--sky);color:var(--white);font-size:14px;font-weight:700;display:flex;align-items:center;justify-content:center}

.site-footer{position:absolute;left:0;top:2296px;width:1200px;height:237px;background:var(--pale)}
.footer-brand{position:absolute;left:58px;top:2380px;display:flex;align-items:center;gap:10px;color:var(--white);font-weight:700;font-size:20px;letter-spacing:1px}
.footer-brand .brand-dot{width:46px;height:46px}
.partner{position:absolute;top:2336px;height:58px}
.footer-nav{position:absolute;left:448px;top:2438px;display:flex;gap:44px;font-size:16px;font-weight:500;color:#1a1a1a}
.copyright{position:absolute;left:448px;top:2482px;font-size:12px;color:#333}
</style>
</head>
<body>

<header class="site-header">
  <div class="brand"><span class="brand-dot"></span>WARD BRIDGE CARE</div>
  <nav class="main-nav">
    <span class="active">HOME</span><span>ABOUT US</span><span>PRESENTATIONS &amp; PUBLICATIONS</span><span>MORE</span>
  </nav>
  <div class="login-btn">LOGIN</div>
</header>

<svg class="hero" viewBox="0 0 1200 520">
  <defs>
    <radialGradient id="gLeft" cx="0.4" cy="0.4" r="0.7"><stop offset="0" stop-color="#8fb3ee"/><stop offset="1" stop-color="#2d63c9"/></radialGradient>
    <radialGradient id="gMid" cx="0.5" cy="0.45" r="0.7"><stop offset="0" stop-color="#b6cff5"/><stop offset="1" stop-color="#5a8fe2"/></radialGradient>
    <radialGradient id="gRight" cx="0.5" cy="0.4" r="0.7"><stop offset="0" stop-color="#9dbdf0"/><stop offset="1" stop-color="#3a72d4"/></radialGradient>
  </defs>
  <circle cx="265" cy="260" r="246" fill="url(#gLeft)" role="img" aria-label="Photo of a magnifying glass over the word health"/>
  <circle cx="935" cy="260" r="246" fill="url(#gRight)" role="img" aria-label="Photo of a stethoscope over a line chart"/>
  <circle cx="600" cy="260" r="171" fill="#ffffff"/>
  <circle cx="600" cy="260" r="145" fill="url(#gMid)" role="img" aria-label="Photo of hands holding a heart with a heartbeat line"/>
</svg>
<div class="hero-dots"><span></span><span></span><span class="on"></span><span></span><span></span></div>

<h1 class="section-title" style="top:676px">WELCOME TO<span class="sub">THE CRITICAL CARE RESEARCH</span></h1>
<div class="title-bar" style="top:818px"></div>
<p class="intro">We are a multi-disciplinary group of clinician-researchers passionate about studying<br>novel medical technologies aimed at improving outcomes of critically ill patients.<br>Take a look around to learn more about our research!</p>

<article class="team-card" style="left:23px">
  <div class="team-photo" role="img" aria-label="Portrait of Helena Varga" style="background:#b7b2a8"></div>
  <h3 class="team-name">Helena Varga</h3>
  <p class="team-bio">Helena works as a Respiratory Therapist at Northgate Hospital and is simul-taneously pursuing a PhD at Westvale University, studying</p>
  <div class="read-btn">READ MORE</div>
</article>
<article class="team-card" style="left:316px">
  <div class="team-photo" role="img" aria-label="Portrait of Dr. Mateo Lindqvist" style="background:#9ea3ac"></div>
  <h3 class="team-name">Dr. Mateo Lindqvist</h3>
  <p class="team-bio">Mateo completed his medical training and neurosurgical residency in Brazil – where he worked as a neurosurgeon until 2016.</p>
  <div class="read-btn">READ MORE</div>
</article>
<article class="team-card" style="left:610px">
  <div class="team-photo" role="img" aria-label="Portrait of Dario Ocampo" style="background:#8a7c66"></div>
  <h3 class="team-name">Dario Ocampo</h3>
  <p class="team-bio">Dario is working as a Respiratory Thera-pist at Northgate Hospital and Harborview Hospital, as well as pursuing his PhD at Westvale by studying</p>
  <div class="read-btn">READ MORE</div>
</article>
<article class="team-card" style="left:903px">
  <div class="team-photo" role="img" aria-label="Portrait of Renata Holloway" style="background:#6f7d95"></div>
  <h3 class="team-name">Renata Holloway</h3>
  <p class="team-bio">Renata works as specialized registered nurse in the cardiac ICU at Northgate Hospital. Since obtaining her MSc. at Branmoor University,</p>
  <div class="read-btn">READ MORE</div>
</article>

<svg class="abs" style="left:548px;top:1493px" width="104" height="46" viewBox="0 0 104 46" aria-label="Previous and next">
  <circle cx="23" cy="23" r="21.5" fill="none" stroke="#333" stroke-width="1.5"/>
  <polyline points="27,14 18,23 27,32" fill="none" stroke="#333" stroke-width="2"/>
  <circle cx="80" cy="23" r="21.5" fill="none" stroke="#333" stroke-width="1.5"/>
  <polyline points="76,14 85,23 76,32" fill="none" stroke="#333" stroke-width="2"/>
</svg>

<h2 class="section-title" style="top:1640px">RECENT PRESENTATIONS<span class="sub">&amp; PUBLICATIONS</span></h2>
<div class="title-bar" style="top:1782px"></div>

<article class="pub-card" style="left:143px">
  <div class="pub-date">May 2020</div>
  <h4 class="pub-title">Negative Hippocampal Turnover Index After 50 Hours of Gold Standard Mechanical Ventilation in a Pre-Clinical Pig Model</h4>
  <p class="pub-meta">DOI: 10.5555/awf-confer-ence.2020.114.2_MeetingAbstracts.B3021<br>Conference: Airway Forum 2020</p>
</article>
<article class="pub-card" style="left:454px">
  <div class="pub-date">Dec 2019</div>
  <h4 class="pub-title">Better PAO2/FIO2 with Temporary Transvenous Neurostimulation Versus Mechanical Ventilation Alone</h4>
  <p class="pub-meta">DOI: 10.5555/01.iwr.0000518204.33720.17<br>Intensive Ward Reports 48.562</p>
</article>
<article class="pub-card" style="left:765px">
  <div class="pub-date">Sep 2020</div>
  <h4 class="pub-title">Temporary Transvenous Diaphragm Neurostimulation Therapy with Mechanical Ventilation Mitigates Atrophy in all Diaphragm Myofiber Types</h4>
  <p class="pub-meta">DOI: 10.5555/j.lwk.2020.06.4412<br>Conference: Lungweek Summit</p>
</article>

<div class="harbor-btn">FIND US ON STUDY HARBOR!</div>

<footer class="site-footer"></footer>
<svg class="abs" style="left:0;top:2296px" width="420" height="237" viewBox="0 0 420 237" aria-hidden="true">
  <polygon points="0,0 418,0 314,237 0,237" fill="#0b35a3"/>
</svg>
<div class="footer-brand"><span class="brand-dot"></span>WARD BRIDGE CARE</div>
<div class="partner" role="img" aria-label="University partner badge" style="left:449px;width:117px;background:#7f141c"></div>
<div class="partner" role="img" aria-label="Health authority partner badge" style="left:585px;width:66px;border-radius:50%;background:#e0442a"></div>
<nav class="footer-nav"><span>HOME</span><span>ABOUT US</span><span>PRESENTATIONS &amp; PUBLICATIONS</span><span>MORE</span></nav>
<p class="copyright">© 2021 by Ward Bridge Care Research Group.All Rights Reserved</p>

</body>
</html>
```